Flu 2019

Lockridge Regional Hospital is hosting a health fair/flu shot clinic this Fall. What she'd like to convey is the following:

Health Fair & Flu Clinic 2019
At the following locations from 10am - 1pm
Fenwick - September 25 at Courthouse in Fenwick
Eden - October 2 at Harlow Multipurpose Center
Menard - October 9 at Tasker Community Center
No cost flu shots available. Please bring insurance information.
Door prizes - Giveaways - Treats
Brought to you by Lockridge Regional Hospital

We would like to highlight the health fair which will be free to the community. We would like to also highlight the flu clinic; however, the no cost/bring insurance needs to be in smaller print.

```html
<!DOCTYPE html>
<html lang="en">
<head>
<meta charset="utf-8">
<title>Health Fair &amp; Flu Clinic 2019 — Lockridge Regional Hospital</title>
<link rel="stylesheet" href="https://fonts.googleapis.com/css2?family=Open+Sans:wght@600;700&family=Cinzel:wght@400&display=swap">
<style>
  :root {
    --teal: #14919e;
    --teal-text: #17909d;
    --cyan: #5ccbd6;
    --blush: #f7e6e0;
    --blush-deep: #e9c4bd;
    --white: #ffffff;
    --ink: #2a2a2a;
    --backdrop: #f6dccd;
  }
  * { margin: 0; padding: 0; box-sizing: border-box; }
  html, body { width: 1200px; height: 800px; overflow: hidden; background: var(--backdrop); }
  .poster {
    position: absolute; left: 356px; top: 40px;
    width: 603px; height: 890px;
    transform: scale(0.809); transform-origin: top left;
    overflow: hidden; background: var(--blush);
    font-family: "Open Sans", Arial, sans-serif;
    box-shadow: 0 10px 24px rgba(120, 70, 50, 0.25);
  }
  .poster > * { position: absolute; }
  .hero-photo {
    left: 0; top: 0; width: 603px; height: 310px;
    background: linear-gradient(100deg, #e7e5e4 0%, #f4f1ef 35%, #d9d4d2 55%, #f2efee 75%, #cfcac8 100%);
  }
  .heart-photo {
    left: 0; top: 440px; width: 603px; height: 360px;
    background: radial-gradient(ellipse at 45% 50%, var(--blush-deep) 0%, #f1d6cf 40%, var(--blush) 75%);
  }
  .brand-disc {
    left: -120px; top: -150px; width: 272px; height: 296px; border-radius: 50%;
    background: rgba(255,255,255,0.85); border: 4px solid #b9b9b9;
  }
  .brand-name {
    left: 10px; top: 36px; width: 130px;
    font-weight: 700; font-size: 15px; line-height: 1.15; color: var(--ink);
  }
  .waves { left: 0; top: 0; width: 603px; height: 890px; }
  .headline {
    left: 0; top: 320px; width: 603px; text-align: center;
    color: var(--white); font-weight: 700; font-size: 36px; letter-spacing: 2.5px; line-height: 50px;
  }
  .byline {
    left: 0; top: 416px; width: 503px; text-align: right;
    color: var(--white); font-weight: 700; font-size: 11px; letter-spacing: 0.6px;
  }
  .hours {
    left: 57px; top: 503px; color: var(--teal-text);
    font-weight: 700; font-size: 20px; letter-spacing: 2px;
  }
  .venues { left: 40px; top: 543px; list-style: none; }
  .venue {
    position: relative; padding-left: 20px; margin-bottom: 15px;
    color: var(--teal-text); font-weight: 700; font-size: 15px; line-height: 19px; letter-spacing: 1.3px;
  }
  .venue::before {
    content: ""; position: absolute; left: 0; top: 5px;
    width: 11px; height: 11px; border-radius: 50%; background: var(--cyan);
  }
  .motto {
    left: 300px; top: 502px; width: 300px; text-align: center;
    font-family: "Cinzel", Georgia, serif; font-size: 42px; line-height: 50px;
    letter-spacing: 3px; color: var(--teal-text);
  }
  .perks {
    left: 0; top: 766px; width: 603px; text-align: center;
    color: var(--teal-text); font-weight: 700; font-size: 19px; letter-spacing: 1.3px;
  }
  .notice-bar {
    left: 0; top: 795px; width: 603px; height: 95px; background: var(--teal);
    color: var(--white); text-align: center; font-weight: 700; font-size: 18px;
    letter-spacing: 1.4px; line-height: 33px; padding-top: 15px;
  }
</style>
</head>
<body>
  <article class="poster">
    <div class="hero-photo" role="img" aria-label="Photo of two doctors holding up stethoscopes"></div>
    <div class="heart-photo" role="img" aria-label="Faint photo of hands holding a red heart with a heartbeat line"></div>

    <svg class="waves" viewBox="0 0 603 890" aria-hidden="true">
      <path d="M0 255 Q300 330 603 228 L603 478 Q330 410 0 482 Z" fill="var(--teal)"/>
      <path d="M300 298 Q470 290 603 228 L603 240 Q470 300 300 298 Z" fill="var(--cyan)"/>
      <path d="M0 482 Q330 410 603 478 L603 492 Q330 428 0 488 Z" fill="#b9b9b9" opacity="0.8"/>
      <path d="M360 440 Q500 445 603 490 L603 505 Q500 455 360 440 Z" fill="var(--cyan)"/>
    </svg>

    <div class="brand-disc"></div>
    <div class="brand-name">Lockridge Regional Hospital</div>

    <h1 class="headline">HEALTH FAIR<br>&amp; FLU CLINIC 2019</h1>
    <p class="byline">BY LOCKRIDGE REGIONAL HOSPITAL</p>

    <p class="hours">10AM - 1PM</p>
    <ul class="venues">
      <li class="venue">SEPTEMBER<br>25 AT COURTHOUSE<br>IN FENWICK</li>
      <li class="venue">OCTOBER<br>2 AT HARLOW<br>MULTIPURPOSE CENTER</li>
      <li class="venue">OCTOBER<br>9 AT TASKER<br>COMMUNITY CENTER</li>
    </ul>

    <p class="motto">YOUR<br>HEALTH<br>IS<br>OUR<br>PRIORITY</p>

    <p class="perks">DOOR PRIZES - GIVEAWAYS - TREATS</p>

    <footer class="notice-bar">NO COST FLU SHOTS AVAILABLE<br>PLEASE BRING INSURANCE INFORMATION</footer>
  </article>
</body>
</html>
```